Most captivating card ever!

Life Coach - Professional Adventurer - Entrepreneur
I need the worlds most amazing business card for my personal brand. This business card will mostly be used to give to prospective clients for life coaching and business coaching.
Be creative, be adventurous. It needs to stand out. Make people say.. I need this guy!
My background is as an entrepreneur and professional adventurer undertaking extreme expeditions. I am now moving into life coaching.
No specific design ideas, so you have full creativity. Show me your best.
Industry/Entity Type
Life Coaching
Contact Information for Business Card
Dan Pellow
itsdanp.com.au
0468215903
Colors
Designer to choose colors to be used in the design.
Look and feel

```html
<!DOCTYPE html>
<html lang="en">
<head>
<meta charset="utf-8">
<title>Dan Pellow – Business Card</title>
<link rel="stylesheet" href="https://fonts.googleapis.com/css2?family=Nunito:wght@400;500&display=swap">
<style>
  :root {
    --brand-red: #ed1c24;
    --ink: #111111;
    --paper: #ffffff;
    --canvas: #ffffff;
  }
  * { box-sizing: border-box; margin: 0; padding: 0; }
  html, body {
    width: 1200px;
    height: 1000px;
    overflow: hidden;
    background: var(--canvas);
    font-family: "Nunito", Arial, sans-serif;
  }
  .canvas { position: relative; width: 1200px; height: 1000px; }

  .card {
    position: absolute;
    left: 359px;
    width: 482px;
    height: 275px;
    overflow: hidden;
  }
  .card--front { top: 179px; background: var(--paper); border: 1px solid #f0f0f0; }
  .card--back  { top: 546px; background: var(--brand-red); }

  .front__mark {
    position: absolute;
    left: 62px;
    top: 64px;
    width: 32px;
    height: 32px;
  }
  .front__name {
    position: absolute;
    left: 33px;
    top: 134px;
    font-size: 26px;
    font-weight: 400;
    color: var(--brand-red);
    letter-spacing: 0.2px;
  }
  .front__roles {
    position: absolute;
    left: 34px;
    top: 170px;
    font-size: 12.5px;
    font-weight: 500;
    color: var(--ink);
  }
  .front__contact {
    position: absolute;
    left: 34px;
    top: 190px;
    font-size: 13px;
    line-height: 19px;
    color: var(--brand-red);
    list-style: none;
  }
  .front__band {
    position: absolute;
    left: 0;
    bottom: 0;
    width: 100%;
    height: 15px;
    background: var(--brand-red);
  }

  .back__identity {
    position: absolute;
    inset: 0;
    display: flex;
    flex-direction: column;
    align-items: center;
    justify-content: center;
    gap: 14px;
  }
  .back__mark { width: 26px; height: 26px; }
  .back__name {
    font-size: 30px;
    font-weight: 400;
    color: var(--paper);
    letter-spacing: 0.5px;
  }
</style>
</head>
<body>
<main class="canvas">
  <section class="card card--front" aria-label="Business card front">
    <svg class="front__mark" viewBox="0 0 32 32" aria-hidden="true">
      <circle cx="16" cy="16" r="16" fill="var(--brand-red)"/>
    </svg>
    <h1 class="front__name">Dan Pellow</h1>
    <p class="front__roles">Life Coach - Professional Adventurer - Entrepreneur</p>
    <ul class="front__contact">
      <li>itsdanp.com.au</li>
      <li>0468215903</li>
    </ul>
    <div class="front__band"></div>
  </section>

  <section class="card card--back" aria-label="Business card back">
    <div class="back__identity">
      <svg class="back__mark" viewBox="0 0 26 26" aria-hidden="true">
        <circle cx="13" cy="13" r="13" fill="var(--paper)"/>
      </svg>
      <p class="back__name">Dan Pellow</p>
    </div>
  </section>
</main>
</body>
</html>
```